Hotel Business Card Project

Amber Crest Hotel will be a premium boutique hotel in Dhaka, Bangladesh. The hotel will offer the finest amenities and facilities available on the market, and the cost per room investment will far exceed other 5-star hotels currently in the market.

As a result, we wanted the business card to reflect that premium/luxurious/upscale feel, and also be elegant and hospitable at the same time.

The name 'Amber Crest' is derived from the fact that Bangladesh has 6 distinct seasons (you can get more information online if required, or contact me about it). The leaves in the logo has the tree because trees give people shade, protection and safety (just like our hotel would try to give).

Target Market(s)

Business professionals, guests

Industry/Entity Type

Investment

Requirements
Must have
• Elegant, Classy and very attractive business card.

Must be editable to enter specific Names, Positions, Phone numbers and email later on.
Nice to have
• The address would be: House 47, Road 23, Lakeview 5, Dhaka 1208, Bangladesh

Slogan- Luxury Redefined

```html
<!DOCTYPE html>
<html lang="en">
<head>
<meta charset="utf-8">
<title>Amber Crest Hotel – Business Cards</title>
<link rel="stylesheet" href="https://fonts.googleapis.com/css2?family=Cinzel:wght@500&family=Arimo:wght@400;700&display=swap">
<style>
  :root {
    --backdrop: #d9d9d9;
    --card-white: #ffffff;
    --brown: #3b2116;
    --amber: #cd742c;
    --ink: #3a2a22;
    --ink-soft: #6a6a6a;
    --mark-grey: #6d6d6d;
    --light: #ffffff;
  }
  * { box-sizing: border-box; margin: 0; padding: 0; }
  html, body {
    width: 1200px; height: 804px; overflow: hidden;
    background: var(--backdrop);
  }
  .canvas { position: relative; width: 1200px; height: 804px; }

  .card {
    position: absolute;
    width: 525px; height: 298px;
    border-radius: 28px;
    overflow: hidden;
  }
  .card--front { left: 48px; top: 65px; background: var(--card-white); }
  .card--brown-plain { left: 628px; top: 67px; background: var(--brown); }
  .card--brown-colour { left: 48px; top: 432px; background: var(--brown); }
  .card--amber { left: 628px; top: 432px; background: var(--amber); }

  /* Hotel name block */
  .brand {
    position: absolute;
    display: flex; flex-direction: column; align-items: center;
    font-family: "Cinzel", serif; font-weight: 500;
    color: var(--light);
  }
  .brand__dot {
    width: 110px; height: 110px; border-radius: 50%;
    background: currentColor; opacity: 1;
    margin-bottom: 26px;
  }
  .brand__name { font-size: 44px; letter-spacing: 1px; line-height: 1; white-space: nowrap; }
  .brand__sub { font-size: 14px; letter-spacing: 2px; margin-top: 6px; }

  .card--front .brand { left: 20px; top: 36px; width: 270px; color: var(--mark-grey); }
  .card--front .brand__dot { width: 90px; height: 90px; margin-bottom: 48px; }
  .card--front .brand__name { font-size: 30px; }
  .card--front .brand__sub { font-size: 11px; margin-top: 3px; }

  .card--brown-plain .brand,
  .card--brown-colour .brand,
  .card--amber .brand { left: 0; right: 0; top: 44px; }

  /* Contact block */
  .contact {
    position: absolute; left: 285px; top: 50px;
    font-family: "Arimo", sans-serif; color: var(--ink-soft);
    font-size: 13.5px; line-height: 18px;
  }
  .contact__name { font-weight: 700; font-size: 16px; color: var(--ink); line-height: 20px; }
  .contact__title { margin-bottom: 46px; }
  .contact__address { margin-bottom: 22px; }
  .contact__row { display: flex; align-items: center; gap: 4px; margin-bottom: 3px; }
  .contact__row svg { width: 12px; height: 12px; flex: none; }
</style>
</head>
<body>
<main class="canvas">

  <section class="card card--front" aria-label="Business card front">
    <div class="brand">
      <span class="brand__dot" aria-hidden="true"></span>
      <span class="brand__name">AMBER CREST</span>
      <span class="brand__sub">HOTEL</span>
    </div>
    <div class="contact">
      <p class="contact__name">Your Name</p>
      <p class="contact__title">Title</p>
      <p class="contact__address">House 47, Road 23<br>Lakeview 5, Dhaka 1208<br>Bangladesh</p>
      <p class="contact__row">
        <svg viewBox="0 0 12 12" aria-hidden="true"><circle cx="6" cy="6" r="5.2" fill="none" stroke="#555" stroke-width="1"/><path d="M4 3.2l1 1.4-.6.8c.4.9 1 1.5 1.9 1.9l.8-.6 1.4 1-.6 1.1C5.8 8.6 3.4 6.2 3 4.1z" fill="#555"/></svg>
        123-456-7890
      </p>
      <p class="contact__row">
        <svg viewBox="0 0 12 12" aria-hidden="true"><rect x="1" y="3" width="10" height="7" fill="none" stroke="#555" stroke-width="1.2"/><path d="M1 3l5 4 5-4" fill="none" stroke="#555" stroke-width="1.2"/></svg>
        info@ambercrestmail.com
      </p>
      <p class="contact__row">
        <svg viewBox="0 0 12 12" aria-hidden="true"><circle cx="6" cy="6" r="5" fill="none" stroke="#555" stroke-width="1"/><ellipse cx="6" cy="6" rx="2.2" ry="5" fill="none" stroke="#555" stroke-width="0.9"/><path d="M1 6h10" stroke="#555" stroke-width="0.9"/></svg>
        www.website.com
      </p>
    </div>
  </section>

  <section class="card card--brown-plain" aria-label="Business card back, brown">
    <div class="brand">
      <span class="brand__dot" aria-hidden="true"></span>
      <span class="brand__name">AMBER CREST</span>
      <span class="brand__sub">HOTEL</span>
    </div>
  </section>

  <section class="card card--brown-colour" aria-label="Business card back, brown alternate">
    <div class="brand">
      <span class="brand__dot" aria-hidden="true"></span>
      <span class="brand__name">AMBER CREST</span>
      <span class="brand__sub">HOTEL</span>
    </div>
  </section>

  <section class="card card--amber" aria-label="Business card back, amber">
    <div class="brand">
      <span class="brand__dot" aria-hidden="true"></span>
      <span class="brand__name">AMBER CREST</span>
      <span class="brand__sub">HOTEL</span>
    </div>
  </section>

</main>
</body>
</html>
```